Template for Orvalen Advisory PowerPoint

We would like to create a new template for PowerPoint based on our current logo and graphic design guidelines. The template should reflect our corporate identity and be easy to use to create different kind of PowerPoint presentations for different kind of customers. The current design guideline that are attached reflect the "old" look of the PPT design and is only to be seen as a reference.
Orvalen Advisory is a Management consulting company working within both public and private sector. We focus on strategic business development and work in close cooperation with the customer to make sure it is the customer that will become the hero, our work is to support and guide them to the top.
The design should reflect a modern company working in close cooperation with our customers to help them innovate and describe their future business model, and also help them to reach that goal!
Words and taglines that we use. Passion for the future. The power of the organisation. Power of thoughts. Inspiration. Engagement.
What we have in mind is a modern, clean and elegant design based on our current logo. Orvalen Advisory is a Swedish Company working primarily on the Swedish market so the template must be possible to translate to Swedish (however the design can be done in english and be translated later)

Project Deadline Extended
Reason: I would like to extend the deadline to receive some more alternatives!

Project Deadline Extended
Reason: I'm out travelling and would like to extend the timeline to be able to choose the right design for our template. /Henrik

Target Market(s)

Our target market is within both private and public sector. Our main focus is CxO level executives within our clients organisation.

Industry/Entity Type

Management Consulting

Font styles to use
Sans Serif

Colors

Designer to choose colors to be used in the design.

Requirements
Must have
• A PPT template that contains both slides for traditional text and graphic. We like to work a lot with graphical presentations and try to limit the text on our slides to a minimum.
Nice to have
• Slides for different chapters within the presentation. Slides for powerful one-liners. Title slides. Thank you slides at the end.
Should not have
• Massive text....

```html
<!DOCTYPE html>
<html lang="en">
<head>
<meta charset="utf-8">
<title>Orvalen Advisory – Presentation Template Overview</title>
<link href="https://fonts.googleapis.com/css2?family=Arimo:wght@400;700&display=swap" rel="stylesheet">
<style>
:root{
  --crimson:#c0143c;
  --blue:#1b5a8a;
  --green:#6b9a3b;
  --olive:#8c8a5c;
  --grey:#a3a3a3;
  --ink:#333;
  --board:#d0d1d9;
  --board-light:#e3e3ea;
  --lavender:#c9c1e0;
  --rock:#6d6156;
  --office:#b7a994;
}
*{box-sizing:border-box;margin:0;padding:0}
html,body{width:1200px;height:854px;overflow:hidden;background:var(--board)}
body{font-family:"Arimo",Arial,sans-serif;color:var(--ink)}
.canvas{position:relative;width:1200px;height:854px;overflow:hidden;background:var(--board)}
.canvas .lower{position:absolute;left:0;top:428px;width:1172px;height:426px;background:var(--board-light)}
.canvas .edge{position:absolute;right:0;top:0;width:28px;height:854px;background:var(--lavender)}

.slide{position:absolute;width:246px;height:186px;background:#fff;overflow:hidden;box-shadow:0 1px 3px rgba(0,0,0,.35)}
.num{position:absolute;font-size:10px;font-weight:700;color:#444;width:20px;text-align:right}
.abs{position:absolute}

.photo-mountain{background:linear-gradient(180deg,#23407e 0%,#4d6aa3 30%,#d9dde6 45%,#8a7f74 60%,var(--rock) 100%)}
.photo-office{background:linear-gradient(135deg,#d9cbb4 0%,var(--office) 45%,#4a4d57 100%)}
.photo-board{background:linear-gradient(100deg,#e8e6e1 0%,#c7b8a2 45%,#f2f1ee 100%)}
.photo-portrait{background:linear-gradient(180deg,#9a2a34 0%,#6b5b55 45%,#3c3f47 100%)}

.hd{position:absolute;left:20px;top:12px;font-size:10.5px;color:var(--crimson);padding-left:9px;line-height:1}
.hd::before{content:"";position:absolute;left:0;top:1px;width:7px;height:8px;background:var(--green);clip-path:polygon(0 100%,100% 0,100% 100%)}
.hd.light{color:#fff}
.hd.light::before{background:#fff}
.brand{position:absolute;right:10px;top:13px;font-size:6.5px;color:#555;line-height:1}
.brand-band{position:absolute;background:var(--crimson)}
.brand-name{position:absolute;font-size:7px;color:#fff;line-height:1}

.ft{position:absolute;left:0;bottom:0;width:100%;height:8px;background:var(--crimson);font-size:3.6px;color:#fff;line-height:8px}
.ft .url{position:absolute;left:0;top:0;height:8px;width:79%;background:var(--blue);padding-left:10px;clip-path:polygon(0 0,97% 0,100% 50%,97% 100%,0 100%)}
.ft .page{position:absolute;right:12px;top:0}

.title{position:absolute;font-size:11px;color:var(--crimson);letter-spacing:.3px}
.lead{position:absolute;font-size:5.6px;line-height:1.45;text-align:center;color:var(--ink)}
.body{position:absolute;font-size:4px;line-height:1.5;color:#222}
.body.c{text-align:center}
.tag{position:absolute;height:9px;font-size:4.2px;line-height:9px;text-align:center;color:#fff;background:var(--crimson);border-radius:1px}
.tag.grey{background:var(--grey);color:#222}
.dot{position:absolute;border-radius:50%;display:flex;align-items:center;justify-content:center}
.dot svg{width:55%;height:55%}
.agenda{position:absolute;left:48px;font-size:6.5px;color:#444}
.agenda b{font-weight:400;color:var(--crimson);display:inline-block;width:24px}
.step{position:absolute;top:52px;width:37px;height:62px;border-radius:4px;color:#fff;font-size:4.2px;text-align:center;padding-top:10px}
.step svg{display:block;width:14px;height:14px;margin:0 auto 5px}
.contact{position:absolute;left:82px;font-size:6px;color:#333;display:flex;align-items:center;gap:8px}
.contact svg{width:6px;height:7px}
</style>
</head>
<body>
<svg width="0" height="0" style="position:absolute" aria-hidden="true">
  <defs>
    <symbol id="ico-case" viewBox="0 0 20 20"><rect x="3" y="6" width="14" height="10" rx="1.5" fill="none" stroke="#fff" stroke-width="1.6"/><path d="M7 6V4h6v2" fill="none" stroke="#fff" stroke-width="1.6"/></symbol>
    <symbol id="ico-gear" viewBox="0 0 20 20"><circle cx="10" cy="10" r="3" fill="none" stroke="#fff" stroke-width="1.6"/><circle cx="10" cy="10" r="6.5" fill="none" stroke="#fff" stroke-width="1.6" stroke-dasharray="2.2 1.6"/></symbol>
    <symbol id="ico-shield" viewBox="0 0 20 20"><path d="M10 3l6 2.5v4c0 4-3 6.5-6 7.5-3-1-6-3.5-6-7.5v-4z" fill="none" stroke="#fff" stroke-width="1.6"/></symbol>
    <symbol id="ico-hand" viewBox="0 0 20 20"><path d="M3 12l4-4 3 2 4-4 3 3-5 5H6z" fill="none" stroke="#fff" stroke-width="1.6" stroke-linejoin="round"/></symbol>
  </defs>
</svg>

<main class="canvas">
  <div class="lower"></div>
  <div class="edge"></div>

  <!-- Row 1 -->
  <section class="slide" style="left:14px;top:5px">
    <div class="abs photo-mountain" style="left:0;top:0;width:246px;height:88px" role="img" aria-label="Mountain pass with prayer flags under a blue sky"></div>
    <div class="brand-band" style="left:20px;top:0;width:38px;height:40px"></div>
    <span class="brand-name" style="left:62px;top:76px">Orvalen</span>
    <h1 class="title" style="left:0;width:246px;top:102px;text-align:center">PRESENTATION TITLE</h1>
    <p class="lead" style="left:24px;width:198px;top:122px">We focus on strategic business development and work in close cooperation with the customer to make sure it is the customer that will become the hero, our work is to support and guide them to the top.</p>
  </section>
  <span class="num" style="left:240px;top:197px">1</span>

  <section class="slide" style="left:316px;top:5px">
    <div class="brand-band" style="left:10px;top:0;width:38px;height:46px"></div>
    <h1 class="title" style="left:70px;top:23px">PRESENTATION TITLE</h1>
    <div class="abs photo-mountain" style="left:0;top:46px;width:246px;height:74px" role="img" aria-label="Mountain pass with prayer flags"></div>
    <span class="brand-name" style="left:10px;top:108px">Orvalen</span>
    <p class="lead" style="left:20px;width:206px;top:140px">Orvalen Advisory Is A Management Consulting Company Working Within Both Public And Private Sector.</p>
  </section>
  <span class="num" style="left:542px;top:197px">2</span>

  <section class="slide" style="left:618px;top:5px">
    <div class="hd" style="left:48px;top:26px">AGENDA</div>
    <p class="agenda" style="top:52px"><b>01.</b>Mission</p>
    <p class="agenda" style="top:74px"><b>02.</b>Today's Situation</p>
    <p class="agenda" style="top:96px"><b>03.</b>Why Invest?</p>
    <div class="abs photo-mountain" style="left:158px;top:0;width:88px;height:186px" role="img" aria-label="Mountain peak with prayer flags"></div>
  </section>
  <span class="num" style="left:844px;top:197px">3</span>

  <section class="slide" style="left:920px;top:5px">
    <div class="hd">Sample Text</div><div class="brand">Orvalen</div>
    <div class="abs photo-office" style="left:75px;top:31px;width:100px;height:54px" role="img" aria-label="Consultants meeting in an office"></div>
    <div class="dot" style="left:48px;top:104px;width:13px;height:13px;background:var(--crimson)"><svg><use href="#ico-case"/></svg></div>
    <div class="dot" style="left:117px;top:104px;width:13px;height:13px;background:var(--crimson)"><svg><use href="#ico-shield"/></svg></div>
    <div class="dot" style="left:194px;top:100px;width:13px;height:13px;background:var(--crimson)"><svg><use href="#ico-hand"/></svg></div>
    <div class="tag grey" style="left:35px;top:120px;width:38px">Sample Text</div>
    <div class="tag grey" style="left:104px;top:120px;width:38px">Sample Text</div>
    <div class="tag grey" style="left:181px;top:116px;width:38px">Sample Text</div>
    <p class="body c" style="left:24px;top:138px;width:58px">We focus on strategic business become the hero, our work is to support and guide them to the top.</p>
    <p class="body c" style="left:94px;top:138px;width:58px">We focus on strategic business become the hero, our work is to support and guide them to the top.</p>
    <p class="body c" style="left:170px;top:134px;width:58px">We focus on strategic business become the hero, our work is to support and guide them to the top.</p>
    <footer class="ft"><span class="url">www.orvalen-advisory.se</span><span class="page">Page • 4</span></footer>
  </section>
  <span class="num" style="left:1146px;top:197px">4</span>

  <!-- Row 2 -->
  <section class="slide" style="left:14px;top:223px">
    <div class="hd">Sample Text</div><div class="brand">Orvalen</div>
    <div class="abs photo-board" style="left:40px;top:34px;width:172px;height:71px" role="img" aria-label="Consultant drawing a diagram on a whiteboard"></div>
    <p class="body" style="left:32px;top:122px;width:108px">We focus on strategic business development and work in close cooperation with the customer to make sure it is the customer that will become the hero, our work is to support and guide them to the top.</p>
    <div class="dot" style="left:188px;top:112px;width:13px;height:13px;background:var(--crimson)"><svg><use href="#ico-hand"/></svg></div>
    <div class="tag grey" style="left:176px;top:130px;width:38px">Sample Text</div>
    <p class="body c" style="left:166px;top:145px;width:58px">We focus on strategic business become the hero, our work is to support and guide them to the top.</p>
    <footer class="ft"><span class="url">www.orvalen-advisory.se</span><span class="page">Page • 4</span></footer>
  </section>
  <span class="num" style="left:240px;top:415px">5</span>

  <section class="slide" style="left:316px;top:223px">
    <div class="hd">Sample Text</div><div class="brand">Orvalen</div>
    <div class="abs photo-office" style="left:19px;top:34px;width:217px;height:64px" role="img" aria-label="Consultants in discussion around a table"></div>
    <div class="dot" style="left:43px;top:86px;width:24px;height:24px;background:var(--green);border:1.5px solid #fff"><svg><use href="#ico-case"/></svg></div>
    <div class="dot" style="left:111px;top:86px;width:24px;height:24px;background:var(--blue);border:1.5px solid #fff"><svg><use href="#ico-shield"/></svg></div>
    <div class="dot" style="left:180px;top:86px;width:24px;height:24px;background:var(--olive);border:1.5px solid #fff"><svg><use href="#ico-gear"/></svg></div>
    <div class="tag" style="left:32px;top:117px;width:46px">Sample Text</div>
    <div class="tag" style="left:100px;top:117px;width:46px">Sample Text</div>
    <div class="tag" style="left:169px;top:117px;width:46px">Sample Text</div>
    <p class="body c" style="left:26px;top:132px;width:58px">We focus on strategic business become the hero, our work is to support and guide them to the top.</p>
    <p class="body c" style="left:94px;top:132px;width:58px">We focus on strategic business become the hero, our work is to support and guide them to the top.</p>
    <p class="body c" style="left:163px;top:132px;width:58px">We focus on strategic business become the hero, our work is to support and guide them to the top.</p>
    <footer class="ft"><span class="url">www.orvalen-advisory.se</span><span class="page">Page • 4</span></footer>
  </section>
  <span class="num" style="left:542px;top:415px">6</span>

  <section class="slide" style="left:618px;top:223px">
    <div class="abs photo-board" style="left:0;top:0;width:246px;height:186px" role="img" aria-label="Consultant sketching ideas on a whiteboard"></div>
    <div class="abs" style="left:107px;top:65px;width:139px;height:92px;background:var(--crimson)"></div>
    <div class="hd light" style="left:116px;top:76px">Sample Text</div>
    <p class="body c" style="left:114px;top:95px;width:126px;color:#fff">We focus on strategic business development and work in close cooperation with the customer to make sure it is the customer that will become the hero, our work is to support and guide them to the top.</p>
    <footer class="ft"><span class="url">www.orvalen-advisory.se</span><span class="page">Page • 4</span></footer>
  </section>
  <span class="num" style="left:844px;top:415px">7</span>

  <section class="slide" style="left:920px;top:223px">
    <div class="abs" style="left:0;top:0;width:43px;height:186px;background:var(--crimson)"></div>
    <div class="hd" style="left:52px;top:26px">Sample Text</div>
    <div class="abs photo-portrait" style="left:24px;top:49px;width:72px;height:95px" role="img" aria-label="Portrait of a consultant"></div>
    <p class="abs" style="left:118px;top:48px;font-size:5px;color:var(--crimson)">Name</p>
    <p class="abs" style="left:118px;top:57px;font-size:4.5px;color:#333">Designation</p>
    <p class="body" style="left:118px;top:68px;width:110px">We focus on strategic business development and work in close cooperation with the customer that will become the hero, our work is to support and guide them to the top.</p>
    <svg class="abs" style="left:118px;top:98px" width="92" height="54" viewBox="0 0 92 54" aria-label="Bar chart">
      <line x1="6" y1="2" x2="6" y2="48" stroke="#999" stroke-width=".5"/>
      <line x1="6" y1="48" x2="88" y2="48" stroke="#999" stroke-width=".5"/>
      <g fill="var(--green)">
        <rect x="6" y="4" width="56" height="3"/><rect x="6" y="10" width="48" height="3"/>
        <rect x="6" y="16" width="58" height="3"/><rect x="6" y="22" width="44" height="3"/>
        <rect x="6" y="28" width="60" height="3"/><rect x="6" y="34" width="62" height="3"/>
        <rect x="6" y="40" width="72" height="3"/>
      </g>
    </svg>
    <footer class="ft"><span class="url">www.orvalen-advisory.se</span><span class="page">Page • 4</span></footer>
  </section>
  <span class="num" style="left:1146px;top:415px">8</span>

  <!-- Row 3 -->
  <section class="slide" style="left:14px;top:434px">
    <div class="hd">Sample Text</div><div class="brand">Orvalen</div>
    <svg class="abs" style="left:0;top:44px" width="246" height="80" viewBox="0 0 246 80" aria-hidden="true">
      <polygon points="10,19 196,19 196,1 234,40 196,79 196,61 10,61" fill="#b9b9b9"/>
    </svg>
    <div class="step" style="left:19px;background:var(--green)"><svg><use href="#ico-case"/></svg>Sample Text</div>
    <div class="step" style="left:62px;background:var(--blue)"><svg><use href="#ico-gear"/></svg>Sample Text</div>
    <div class="step" style="left:105px;background:var(--crimson)"><svg><use href="#ico-shield"/></svg>Sample Text</div>
    <div class="step" style="left:148px;background:var(--olive)"><svg><use href="#ico-hand"/></svg>Sample Text</div>
    <p class="abs" style="left:194px;top:81px;font-size:5.5px;font-weight:700;color:#222">RESULT</p>
    <p class="body c" style="left:30px;top:136px;width:186px">We focus on strategic business development and work in close cooperation with the customer to make sure it is the customer that will become the hero, our work is to support and guide them to the top.</p>
    <footer class="ft"><span class="url">www.orvalen-advisory.se</span><span class="page">Page • 4</span></footer>
  </section>
  <span class="num" style="left:240px;top:626px">9</span>

  <section class="slide" style="left:316px;top:434px">
    <div class="hd">Sample Text</div><div class="brand">Orvalen</div>
    <svg class="abs" style="left:0;top:0" width="246" height="186" viewBox="0 0 246 186" font-family="Arimo, Arial, sans-serif" font-size="4.2">
      <line x1="28" y1="79" x2="226" y2="79" stroke="#aaa" stroke-width=".6"/>
      <circle cx="37" cy="79" r="7" fill="#fff" stroke="var(--crimson)" stroke-width="2.5"/>
      <circle cx="77" cy="79" r="3.5" fill="var(--green)"/>
      <circle cx="104" cy="79" r="3.5" fill="var(--blue)"/>
      <circle cx="150" cy="79" r="7" fill="#fff" stroke="var(--crimson)" stroke-width="2.5"/>
      <circle cx="190" cy="79" r="3.5" fill="var(--green)"/>
      <circle cx="212" cy="79" r="3.5" fill="var(--blue)"/>
      <text transform="translate(46 68) rotate(-65)" fill="var(--crimson)">Sample Text</text>
      <text transform="translate(159 68) rotate(-65)" fill="var(--crimson)">Sample Text</text>
      <text transform="translate(75 88) rotate(65)" fill="var(--green)">Sample Text</text>
      <text transform="translate(102 88) rotate(65)" fill="var(--blue)">Sample Text</text>
      <text transform="translate(188 88) rotate(65)" fill="var(--green)">Sample Text</text>
      <text transform="translate(210 88) rotate(65)" fill="var(--blue)">Sample Text</text>
    </svg>
    <p class="body c" style="left:30px;top:137px;width:186px">We focus on strategic business development and work in close cooperation with the customer to make sure it is the customer that will become the hero, our work is to support and guide them to the top.</p>
    <footer class="ft"><span class="url">www.orvalen-advisory.se</span><span class="page">Page • 4</span></footer>
  </section>
  <span class="num" style="left:542px;top:626px">10</span>

  <section class="slide" style="left:618px;top:434px">
    <div class="hd">Sample Text</div><div class="brand">Orvalen</div>
    <svg class="abs" style="left:0;top:0" width="246" height="186" viewBox="0 0 246 186" font-family="Arimo, Arial, sans-serif" font-size="4.2">
      <rect x="10" y="76" width="186" height="4" fill="var(--blue)"/>
      <polygon points="194,72 204,78 194,84" fill="var(--blue)"/>
      <g fill="var(--blue)">
        <rect x="31" y="64" width="3" height="12"/><polygon points="28,66 32.5,60 37,66"/>
        <rect x="91" y="64" width="3" height="12"/><polygon points="88,66 92.5,60 97,66"/>
        <rect x="149" y="64" width="3" height="12"/><polygon points="146,66 150.5,60 155,66"/>
        <rect x="56" y="80" width="3" height="10"/><polygon points="53,88 57.5,94 62,88"/>
        <rect x="117" y="80" width="3" height="10"/><polygon points="114,88 118.5,94 123,88"/>
        <rect x="177" y="80" width="3" height="10"/><polygon points="174,88 178.5,94 183,88"/>
      </g>
      <g fill="var(--crimson)">
        <rect x="18" y="50" width="36" height="8"/><rect x="79" y="50" width="36" height="8"/><rect x="138" y="50" width="36" height="8"/>
        <rect x="41" y="97" width="36" height="8"/><rect x="103" y="97" width="36" height="8"/><rect x="162" y="97" width="36" height="8"/>
        <rect x="206" y="74" width="34" height="8"/>
      </g>
      <g fill="#fff" text-anchor="middle">
        <text x="36" y="55.5">Sample Text</text><text x="97" y="55.5">Sample Text</text><text x="156" y="55.5">Sample Text</text>
        <text x="59" y="102.5">Sample Text</text><text x="121" y="102.5">Sample Text</text><text x="180" y="102.5">Sample Text</text>
        <text x="223" y="79.5">Sample Text</text>
      </g>
    </svg>
    <p class="body c" style="left:30px;top:122px;width:186px">We focus on strategic business development and work in close cooperation with the customer to make sure it is the customer that will become the hero, our work is to support and guide them to the top.</p>
    <footer class="ft"><span class="url">www.orvalen-advisory.se</span><span class="page">Page • 4</span></footer>
  </section>
  <span class="num" style="left:844px;top:626px">11</span>

  <section class="slide" style="left:920px;top:434px">
    <div class="hd">Sample Text</div><div class="brand">Orvalen</div>
    <svg class="abs" style="left:0;top:0" width="246" height="186" viewBox="0 0 246 186" font-family="Arimo, Arial, sans-serif" font-size="4.2">
      <circle cx="32" cy="80" r="20" fill="var(--crimson)"/>
      <circle cx="70" cy="61" r="18" fill="var(--green)"/>
      <circle cx="108" cy="79" r="21" fill="var(--blue)"/>
      <circle cx="162" cy="84" r="31" fill="var(--crimson)"/>
      <circle cx="211" cy="61" r="21" fill="var(--olive)"/>
      <g fill="none" stroke="#fff" stroke-width=".9">
        <rect x="28" y="67" width="8" height="6" rx="1"/>
        <circle cx="70" cy="51" r="3.5" stroke-dasharray="1.4 1"/>
        <path d="M108 65l4 1.6v2.6c0 2.6-2 4.2-4 4.8-2-.6-4-2.2-4-4.8v-2.6z"/>
        <path d="M156 72l3-3 2 1.5 3-3 2 2-4 4h-4z"/>
        <path d="M206 52l3-3 2 1.5 3-3 2 2-4 4h-4z"/>
      </g>
      <g fill="#fff" text-anchor="middle">
        <text x="32" y="85">Sample Text</text><text x="70" y="64">Sample Text</text>
        <text x="108" y="82">Sample Text</text><text x="162" y="87">Sample Text</text>
        <text x="211" y="64">Sample Text</text>
      </g>
    </svg>
    <p class="body c" style="left:30px;top:126px;width:186px">We focus on strategic business development and work in close cooperation with the customer to make sure it is the customer that will become the hero, our work is to support and guide them to the top.</p>
    <footer class="ft"><span class="url">www.orvalen-advisory.se</span><span class="page">Page • 4</span></footer>
  </section>
  <span class="num" style="left:1146px;top:626px">12</span>

  <!-- Row 4 -->
  <section class="slide" style="left:14px;top:652px">
    <div class="hd">Sample Text</div><div class="brand">Orvalen</div>
    <svg class="abs" style="left:0;top:0" width="140" height="150" viewBox="0 0 140 150" font-family="Arimo, Arial, sans-serif" font-size="4.5">
      <g fill="none" stroke-width="8">
        <path d="M49 44a28 28 0 0 1 28 28" stroke="var(--crimson)"/>
        <path d="M77 72a28 28 0 0 1-28 28" stroke="var(--blue)"/>
        <path d="M49 100a28 28 0 0 1-28-28" stroke="var(--crimson)"/>
        <path d="M21 72a28 28 0 0 1 28-28" stroke="var(--blue)"/>
      </g>
      <circle cx="44" cy="72" r="9" fill="var(--crimson)"/>
      <circle cx="54" cy="72" r="9" fill="var(--crimson)" stroke="#fff" stroke-width=".8"/>
      <g fill="#fff" stroke="var(--blue)" stroke-width=".6">
        <circle cx="24" cy="42" r="9"/><circle cx="84" cy="42" r="9"/>
        <circle cx="30" cy="114" r="9"/><circle cx="82" cy="114" r="9"/>
      </g>
      <g fill="var(--crimson)" text-anchor="middle" font-weight="700">
        <text x="24" y="44">20%</text><text x="84" y="44">20%</text>
        <text x="30" y="116">20%</text><text x="82" y="116">20%</text>
      </g>
    </svg>
    <p class="abs" style="left:144px;top:38px;font-size:12px;font-weight:700;color:var(--crimson)">20%</p>
    <p class="body" style="left:144px;top:58px;width:90px">We focus on strategic business development and work in close cooperation with the customer to make sure it is cooperation with the customer to make sure it is the customer that will become the hero, our work is to support and guide them to the top.</p>
    <footer class="ft"><span class="url">www.orvalen-advisory.se</span><span class="page">Page • 4</span></footer>
  </section>

  <section class="slide" style="left:316px;top:652px">
    <div class="hd">Sample Text</div><div class="brand">Orvalen</div>
    <div class="dot" style="left:22px;top:45px;width:15px;height:11px;background:var(--crimson)"><svg><use href="#ico-case"/></svg></div>
    <div class="dot" style="left:22px;top:79px;width:15px;height:11px;background:var(--crimson)"><svg><use href="#ico-shield"/></svg></div>
    <div class="dot" style="left:22px;top:114px;width:15px;height:11px;background:var(--crimson)"><svg><use href="#ico-shield"/></svg></div>
    <p class="body" style="left:45px;top:44px;width:185px">We focus on strategic business development and work in close cooperation with the customer to make sure it is the customer that will become the hero, our work is to support and guide them to the top.</p>
    <p class="body" style="left:45px;top:78px;width:185px">We focus on strategic business development and work in close cooperation with the customer to make sure it is the customer that will become the hero, our work is to support and guide them to the top.</p>
    <p class="body" style="left:45px;top:113px;width:185px">We focus on strategic business development and work in close cooperation with the customer to make sure it is the customer that will become the hero, our work is to support and guide them to the top.</p>
    <footer class="ft"><span class="url">www.orvalen-advisory.se</span><span class="page">Page • 4</span></footer>
  </section>

  <section class="slide" style="left:618px;top:652px">
    <div class="hd">Sample Text</div><div class="brand">Orvalen</div>
    <div class="abs photo-office" style="left:27px;top:32px;width:64px;height:56px" role="img" aria-label="Consultants meeting"></div>
    <div class="abs photo-board" style="left:129px;top:32px;width:67px;height:56px" role="img" aria-label="Consultant at a whiteboard"></div>
    <div class="tag" style="left:27px;top:97px;width:38px">Sample Text</div>
    <div class="tag" style="left:129px;top:97px;width:38px">Sample Text</div>
    <p class="body" style="left:27px;top:113px;width:90px">We focus on strategic business development and work in close cooperation with the customer to make sure it is the customer that will become the hero, our work is to support and guide them to the top.</p>
    <p class="body" style="left:129px;top:113px;width:90px">We focus on strategic business development and work in close cooperation with the customer to make sure it is the customer that will become the hero, our work is to support and guide them to the top.</p>
    <footer class="ft"><span class="url">www.orvalen-advisory.se</span><span class="page">Page • 4</span></footer>
  </section>

  <section class="slide" style="left:920px;top:652px">
    <div class="abs photo-mountain" style="left:0;top:0;width:246px;height:91px" role="img" aria-label="Mountain pass with prayer flags"></div>
    <div class="brand-band" style="left:20px;top:0;width:40px;height:40px"></div>
    <span class="brand-name" style="left:66px;top:79px">Orvalen</span>
    <p class="contact" style="top:113px"><svg viewBox="0 0 12 14"><path d="M6 0a5 5 0 0 1 5 5c0 4-5 9-5 9S1 9 1 5a5 5 0 0 1 5-5z" fill="#222"/><circle cx="6" cy="5" r="1.8" fill="#fff"/></svg>48 Lindell Ave, Riverton, IL 60210</p>
    <p class="contact" style="top:131px"><svg viewBox="0 0 12 14"><path d="M3 1l2 3-1.5 1.5c.8 2 2 3.2 4 4L9 8l3 2-1.5 3C5 12 1 8 0 2.5z" fill="#444"/></svg>Call Us</p>
    <p class="contact" style="top:149px"><svg viewBox="0 0 12 14"><circle cx="6" cy="7" r="5.5" fill="#222"/><rect x="3" y="5" width="6" height="4" fill="#fff"/></svg>Mail Us</p>
  </section>
</main>
</body>
</html>
```